Looking for a high-end business card design for a construction company

We are looking to update our business card design. We are a post-frame construction company that builds custom buildings, commercial spaces, homes, and anything else. We have multiple people working here so we would need something we can easily customize the information for the specific person. We need a name, website, cell phone, office phone as well as social icons. Our colors are black, white, and grey/silver so I would love a black background or something that is more striking than just a traditional white business card. Looking for something that is very professional with a high-end look/feel. I have attached our logos, they can be silver, white, grey, or black.
Industry/Entity Type
Construction
Contact Information for Business Card
Business logo, Name, Cell phone, Office phone, website, social Icons
Colors
Designer to choose only greyscale colors for use in the design.
Look and feel

```html
<!DOCTYPE html>
<html lang="en">
<head>
<meta charset="utf-8">
<title>Kestrel Builders – Business Card</title>
<link href="https://fonts.googleapis.com/css2?family=Open+Sans:wght@400;600;700&display=swap" rel="stylesheet">
<style>
  :root {
    --backdrop: #3b3b3b;
    --card: #141414;
    --silver: #cfcfcf;
    --silver-soft: #9a9a9a;
    --rule: #8c8c8c;
    --emboss: #2a2a2a;
  }
  * { margin: 0; padding: 0; box-sizing: border-box; }
  html, body {
    width: 1200px; height: 801px; overflow: hidden;
    background: var(--backdrop);
    font-family: "Open Sans", Arial, sans-serif;
  }
  .stage {
    width: 1200px; height: 801px;
    display: flex; align-items: center; justify-content: center; gap: 40px;
  }
  .card {
    width: 540px; height: 309px;
    background: var(--card);
    position: relative;
    box-shadow: 0 14px 30px rgba(0,0,0,.45);
  }
  /* Front */
  .card-front { display: flex; align-items: center; }
  .brand {
    width: 250px; padding-left: 40px;
    display: flex; align-items: center; gap: 10px;
  }
  .brand-dot {
    width: 14px; height: 14px; border-radius: 50%;
    background: var(--silver); flex: none;
  }
  .brand-name {
    color: var(--silver); font-weight: 700; font-size: 19px;
    letter-spacing: 1.5px; line-height: 1.15; text-transform: uppercase;
  }
  .divider {
    width: 1px; height: 110px; background: var(--rule);
  }
  .contact { padding-left: 26px; color: var(--silver); }
  .contact-name {
    font-size: 17px; font-weight: 700; letter-spacing: .5px; text-transform: uppercase;
  }
  .contact-title {
    font-size: 13px; color: var(--silver-soft); margin-bottom: 10px;
  }
  .contact-list { list-style: none; font-size: 13px; line-height: 1.6; }
  .contact-list li { display: flex; align-items: center; gap: 8px; }
  .contact-list svg { width: 11px; height: 11px; flex: none; }
  /* Back */
  .card-back { display: flex; align-items: center; justify-content: center; }
  .back-name {
    color: var(--emboss); font-weight: 700; font-size: 30px;
    letter-spacing: 3px; text-transform: uppercase;
  }
</style>
</head>
<body>
<main class="stage">
  <section class="card card-front">
    <div class="brand">
      <span class="brand-dot"></span>
      <span class="brand-name">Kestrel<br>Builders, Inc.</span>
    </div>
    <div class="divider"></div>
    <div class="contact">
      <p class="contact-name">Daniel Harrow</p>
      <p class="contact-title">President</p>
      <ul class="contact-list">
        <li>
          <svg viewBox="0 0 12 12"><rect x="3" y="0.5" width="6" height="11" rx="1" fill="none" stroke="#cfcfcf"/></svg>
          555-014-2270
        </li>
        <li>
          <svg viewBox="0 0 12 12"><path d="M2 1h3l1 3-2 1a7 7 0 0 0 3 3l1-2 3 1v3c-6 0-9-3-9-9z" fill="#cfcfcf"/></svg>
          555-014-2270
        </li>
        <li>
          <svg viewBox="0 0 12 12"><rect x="0.5" y="2" width="11" height="8" fill="#cfcfcf"/><path d="M0.5 2l5.5 4.5L11.5 2" fill="none" stroke="#141414"/></svg>
          dharrow@kestrelbuilders
        </li>
        <li>
          <svg viewBox="0 0 12 12"><circle cx="6" cy="6" r="5.5" fill="#cfcfcf"/><path d="M0.5 6h11M6 .5c-3 3-3 8 0 11M6 .5c3 3 3 8 0 11" fill="none" stroke="#141414" stroke-width=".8"/></svg>
          www.kestrelbuilders.com
        </li>
      </ul>
    </div>
  </section>
  <section class="card card-back">
    <span class="back-name">Kestrel</span>
  </section>
</main>
</body>
</html>
```